Zielgruppe
Wir machen individualisierte Biere mit entsprechend coolen Etiketten-Designs. In diesem Fall ist es ein Geschenk für einen Freund, der heiratet.
Aufgabenstellung
Er hat seiner Verlobten den Heiratsantrag unter Polarlichtern in Island gemacht. Es wäre cool, wenn man karrikativ zwei Menschen, die Hände halten unter Polarlichtern sieht und der oben genannte Name 'Dravek' auf Kyrillisch (serb. für Liebe) in den Polarlichtern integriert ist. Ich habe unten als Inspiration die Webseite der Bierbrauerei angegeben, dort seht ihr den Stil der anderen Designs. Das Etiketten-Format findet ihr im Anhang. Im Anhang findet ihr auch ein Bild von den Polarlichtern, wo er ihr den Heiratsantrag gemacht hat, vielleicht hilft es euch zur Vorstellung.
Website: https://mrvesta.rs/shop/

```html
<!DOCTYPE html>
<html lang="sr">
<head>
<meta charset="utf-8">
<title>MRVESTA – Etiketa</title>
<link rel="stylesheet" href="https://fonts.googleapis.com/css2?family=Jost:wght@400;500&display=swap">
<style>
  :root {
    --paper: #ffffff;
    --ink: #1a1a1a;
    --measure: #e0301e;
    --sky-deep: #2b2a6b;
    --sky-violet: #7a5bc7;
    --aurora-pink: #f06aa8;
    --aurora-orange: #f7a15a;
    --aurora-yellow: #f6e27a;
    --aurora-green: #7fd9b0;
    --snow: #efe3f3;
    --forest: #2d5a63;
  }
  * { margin: 0; padding: 0; box-sizing: border-box; }
  html, body {
    width: 1046px; height: 1200px; overflow: hidden;
    background: var(--paper);
  }
  .label {
    position: relative; width: 1046px; height: 1200px;
    background: var(--paper); color: var(--ink);
    font-family: "Jost", sans-serif;
  }
  .brand {
    position: absolute; top: 56px; left: 0; width: 100%;
    text-align: center;
    font-family: "Jost", sans-serif; font-weight: 500;
    font-size: 92px; line-height: 1; letter-spacing: 0;
  }
  .artwork {
    position: absolute; left: 156px; top: 178px;
    width: 690px; height: 880px;
    background:
      radial-gradient(ellipse 55% 30% at 50% 38%, var(--aurora-yellow) 0%, transparent 70%),
      radial-gradient(ellipse 70% 40% at 70% 30%, var(--aurora-orange) 0%, transparent 70%),
      radial-gradient(ellipse 70% 45% at 25% 32%, var(--aurora-pink) 0%, transparent 72%),
      radial-gradient(ellipse 60% 35% at 40% 55%, var(--aurora-green) 0%, transparent 70%),
      linear-gradient(180deg, var(--sky-deep) 0%, var(--sky-violet) 20%, #b57ad0 45%, var(--forest) 72%, var(--snow) 85%, #d9b7e6 100%);
  }
  .love-word {
    position: absolute; left: 156px; top: 340px; width: 690px;
    text-align: center; color: #ffffff;
    font-family: "Jost", sans-serif; font-weight: 500;
    font-size: 150px; line-height: 1; letter-spacing: 2px;
  }
  .side {
    position: absolute; white-space: nowrap;
    transform-origin: left top; transform: rotate(-90deg);
    font-size: 31px; line-height: 1.3;
  }
  .side-left { left: 60px; top: 1020px; }
  .netto { left: 890px; top: 395px; font-size: 33px; }
  .alcohol { left: 890px; top: 1030px; font-size: 33px; }
  .measure { position: absolute; color: var(--measure); font-size: 30px; }
  .measure-top { left: 885px; top: 505px; }
  .measure-side {
    left: 965px; top: 730px; white-space: nowrap;
    transform-origin: left top; transform: rotate(-90deg);
  }
  .signature-slot {
    position: absolute; left: 908px; top: 568px;
    width: 40px; height: 118px;
    border: 2px solid var(--measure);
  }
  .signature-slot span {
    position: absolute; left: 4px; top: 112px; width: 108px;
    transform-origin: left top; transform: rotate(-90deg);
    color: var(--measure); font-size: 12px; line-height: 1.15;
    text-align: center;
  }
  .beer-name {
    position: absolute; left: 0; top: 1090px; width: 100%;
    text-align: center; font-size: 50px; letter-spacing: 1px;
  }
</style>
</head>
<body>
<main class="label">
  <div class="brand">MRVESTA</div>

  <div class="artwork" role="img" aria-label="Illustration: a couple embracing on snow under colourful northern lights, pine trees at the sides"></div>
  <div class="love-word">дравек</div>

  <div class="side side-left">Specijalno, svetlo Ale pivo.<br>Mutno, nefiltrirano i nepasterizovano.</div>

  <div class="side netto">Netto: 330 ml</div>
  <div class="measure measure-top">0.5 cm</div>
  <div class="signature-slot"><span>Mesto za<br>potpis umetnika</span></div>
  <div class="measure measure-side">1.5 cm</div>
  <div class="side alcohol">5.6% Alk.</div>

  <div class="beer-name">Naziv Piva</div>
</main>
</body>
</html>
```